Pagecraft Design for Fruit & Veggie Swap Site

I need a pagecraft design for the HOME PAGE of a company located in Kona, Hawaii called Leafway Exchange Hawaii. Leafway Exchange Hawaii (LEH) is a site intended to support the local food movement by connecting neighbors in order for them to swap/trade produce from their farm or garden. The purpose of this site is to support sustainable agriculture in Hawaii and encourage community interaction.

The model of the site is similar to:
http://www.harvtrade.me/ (I really like the simple design of this site)
http://www.plotbarter.co.uk/ (I don't like the design of this site, just the functionality. The design is too busy and unbalanced.)
Unlike the two sites listed above, however, LEH is only targeted at people living on the Big Island of Hawaii.

The site is simply intended to be a platform to connect people, then they are free to swap or barter off site, similar to the way postboardly connects people. Users can create "posts" for crops that they have available for swap, which are searchable based on name and location.

I have created a very basic, no-css, dev version of the site to work on the back end, which is located here: http://leafwayexchangehawaii.com/test
Feel free to register and create a test post to get a feel for how it works.

The images I have uploaded are just for ideas and do not have to be in the design.

Target Market(s)

The targeted audience is gardeners and farmers on the Big Island of Hawaii. These people are quite varied in age and technical ability.

Industry/Entity Type

Agriculture

Requirements
Must have
• On the homepage, I would like to have a list of the most recent "posts", displayed as the post title, with the most recent post at the top of the list. In the test site, this is located in the right column, but it doesn't have to be in that location in the final design.

I would also like the option to "Add new listing" to be displayed creatively on the home page. This can be in the form of a graphic that links to a form on another page.

I would also like to have a search box on the homepage. Users can search by crop name and/or location.

The main focal point of the home page will be a Mapsly map application of the Big Island. I am in the process of developing this. You can see the map on the test site, please keep in mind that this map may change slightly in future revisions. Feel free to change the size and styling of the map to fit your design.

I would like the homepage to have a simple and clean layout, making it clear to users how the site works.
For the graphics, I would like to incorporate the "crop circles" idea (yes, like the alien crop circles in fields) with fruits and veggies (including tropical fruit found in Hawaii like banana, coconut, lychee, taro, oranges, as well as traditional vegetables like carrots, lettuce, etc.), and also potentially with the idea of sharing and circulating produce with neighbors.
Please note that those specific fruits and veggies don't need to be used, or that many of them, I was just giving them as examples.

I would also like to have a place on the homepage where users can login/sign up. This can be a login form with a sign up link, or a login link and a sign up link.

I would like the entire design to fit on a page without having to scroll.

Once the site has a substantial user base, I plan to incorporate advertising. Please create a design that will be easy to integrate ads into in the future, most likely in the side bar or footer. I do not want the original design to have ad space, just the ability to add it easily in the future and having it look good with the current design.

```html
<!DOCTYPE html>
<html lang="en">
<head>
<meta charset="utf-8">
<title>Leafway Exchange Hawaii – Home</title>
<link href="https://fonts.googleapis.com/css2?family=Cantarell:wght@400;700&family=Source+Sans+3:wght@400;600&display=swap" rel="stylesheet">
<style>
  :root{
    --topline:#2f67a6;
    --header-top:#8fbbe6;
    --header-bottom:#5f95cc;
    --ink:#111;
    --post-ink:#1f3d4f;
    --field-bg:#ffffff;
    --field-ink:#6b6b6b;
    --btn-top:#5a8fcb;
    --btn-bottom:#2d609f;
    --cta-top:#bcd9f3;
    --cta-bottom:#8fbbe6;
    --panel-line:#d4d8da;
    --side-line:#cfe3e6;
    --map-tone-a:#dfe3e4;
    --map-tone-b:#e9eae2;
    --footer-bg:#f4f3f3;
    --footer-base:#3d3a3a;
    --footer-ink:#333;
    --social:#a9a9a9;
  }
  *{box-sizing:border-box;margin:0;padding:0}
  html,body{width:1200px;height:614px;overflow:hidden;background:#fff}
  body{position:relative;font-family:"Source Sans 3",Arial,sans-serif;color:var(--ink)}

  .site-header{position:absolute;left:0;top:0;width:1200px;height:77px;
    background:linear-gradient(var(--header-top),var(--header-bottom));
    border-top:4px solid var(--topline)}
  .brand{position:absolute;left:114px;top:26px;font-family:"Cantarell",sans-serif;
    font-weight:700;font-size:26px;letter-spacing:0.3px;text-transform:uppercase;color:var(--ink);line-height:1}
  .login-form{position:absolute;left:652px;top:19px;display:flex;gap:9px;align-items:center}
  .login-field{width:154px;height:27px;border:none;border-radius:14px;background:var(--field-bg);
    padding:0 10px;font:12px "Source Sans 3",sans-serif;color:var(--field-ink);display:flex;align-items:center}
  .login-button{width:108px;height:25px;border-radius:13px;border:none;
    background:linear-gradient(var(--btn-top),var(--btn-bottom));color:#fff;
    font:600 13.5px "Source Sans 3",sans-serif;display:flex;align-items:center;justify-content:center}

  .search-box{position:absolute;left:123px;top:94px;width:254px;height:34px;border:1px solid #9a9a9a;
    border-radius:17px;background:#fff;display:flex;align-items:center}
  .search-text{flex:1;padding-left:17px;font-size:11px;color:#444}
  .search-button{width:51px;height:100%;border-left:1px solid #9a9a9a;display:flex;align-items:center;justify-content:center}

  .add-listing{position:absolute;left:853px;top:89px;width:222px;height:43px;border-radius:5px;
    background:linear-gradient(var(--cta-top),var(--cta-bottom));display:flex;align-items:center;
    padding-left:27px;gap:32px;font-size:20px;color:var(--ink)}

  .map-panel{position:absolute;left:125px;top:145px;width:653px;height:375px;border:1px solid var(--panel-line);
    border-radius:8px;background:#fff;box-shadow:0 6px 6px -4px rgba(0,0,0,.18)}
  .map-view{position:absolute;left:14px;top:14px;width:629px;height:347px;
    background:linear-gradient(160deg,var(--map-tone-a),var(--map-tone-b))}

  .latest-posts{position:absolute;left:798px;top:146px;width:281px;height:374px;border:1px solid var(--side-line);
    border-radius:4px;background:#fff;overflow:hidden}
  .latest-posts h2{height:47px;background:linear-gradient(#8cbbe8,#5e94cc);color:#fff;font-weight:400;
    font-size:19px;padding:11px 0 0 14px}
  .post-list{list-style:none;padding:11px 0 0 21px}
  .post-item{display:flex;align-items:center;gap:13px;height:27.6px;font-size:14.5px;color:var(--post-ink)}

  .site-footer{position:absolute;left:0;top:542px;width:1200px;height:63px;background:var(--footer-bg)}
  .copyright{position:absolute;left:137px;top:26px;font-size:11.5px;color:var(--footer-ink)}
  .social-links{position:absolute;left:1008px;top:20px;display:flex;gap:8px}
  .social-dot{width:18px;height:18px;border-radius:50%;background:var(--social)}
  .footer-base{position:absolute;left:0;top:605px;width:1200px;height:9px;background:var(--footer-base)}
</style>
</head>
<body>
  <header class="site-header">
    <div class="brand">Leafway Exchange Hawaii</div>
    <div class="login-form">
      <div class="login-field">Email</div>
      <div class="login-field">Password</div>
      <div class="login-button">Login / Sign up</div>
    </div>
  </header>

  <div class="search-box">
    <span class="search-text">Search by name / Location</span>
    <span class="search-button">
      <svg width="22" height="22" viewBox="0 0 22 22"><circle cx="9" cy="9" r="6.5" fill="none" stroke="#333" stroke-width="2.4"/><line x1="13.8" y1="13.8" x2="19.5" y2="19.5" stroke="#333" stroke-width="3" stroke-linecap="round"/></svg>
    </span>
  </div>

  <div class="add-listing">
    <span>Add new listing</span>
    <svg width="10" height="12" viewBox="0 0 10 12"><path d="M0 0 L10 6 L0 12 Z" fill="#5f95cc"/></svg>
  </div>

  <section class="map-panel">
    <div class="map-view" role="img" aria-label="Interactive map of the Big Island of Hawaii showing produce listings"></div>
  </section>

  <aside class="latest-posts">
    <h2>Latest Posts :</h2>
    <ul class="post-list">
      <li class="post-item"><svg width="16" height="16" viewBox="0 0 16 16"><circle cx="8" cy="8" r="8"/><path d="M6 4.5 L11.5 8 L6 11.5Z" fill="#fff"/></svg>Testing Redirect 1</li>
      <li class="post-item"><svg width="16" height="16" viewBox="0 0 16 16"><circle cx="8" cy="8" r="8"/><path d="M6 4.5 L11.5 8 L6 11.5Z" fill="#fff"/></svg>Testing Redirect 1</li>
      <li class="post-item"><svg width="16" height="16" viewBox="0 0 16 16"><circle cx="8" cy="8" r="8"/><path d="M6 4.5 L11.5 8 L6 11.5Z" fill="#fff"/></svg>Oranges</li>
      <li class="post-item"><svg width="16" height="16" viewBox="0 0 16 16"><circle cx="8" cy="8" r="8"/><path d="M6 4.5 L11.5 8 L6 11.5Z" fill="#fff"/></svg>Lemons</li>
      <li class="post-item"><svg width="16" height="16" viewBox="0 0 16 16"><circle cx="8" cy="8" r="8"/><path d="M6 4.5 L11.5 8 L6 11.5Z" fill="#fff"/></svg>Papaya</li>
      <li class="post-item"><svg width="16" height="16" viewBox="0 0 16 16"><circle cx="8" cy="8" r="8"/><path d="M6 4.5 L11.5 8 L6 11.5Z" fill="#fff"/></svg>Lettuce</li>
      <li class="post-item"><svg width="16" height="16" viewBox="0 0 16 16"><circle cx="8" cy="8" r="8"/><path d="M6 4.5 L11.5 8 L6 11.5Z" fill="#fff"/></svg>Coffee Cherries</li>
      <li class="post-item"><svg width="16" height="16" viewBox="0 0 16 16"><circle cx="8" cy="8" r="8"/><path d="M6 4.5 L11.5 8 L6 11.5Z" fill="#fff"/></svg>Bamboo Plants</li>
      <li class="post-item"><svg width="16" height="16" viewBox="0 0 16 16"><circle cx="8" cy="8" r="8"/><path d="M6 4.5 L11.5 8 L6 11.5Z" fill="#fff"/></svg>Kona Limes</li>
      <li class="post-item"><svg width="16" height="16" viewBox="0 0 16 16"><circle cx="8" cy="8" r="8"/><path d="M6 4.5 L11.5 8 L6 11.5Z" fill="#fff"/></svg>Mango</li>
      <li class="post-item"><svg width="16" height="16" viewBox="0 0 16 16"><circle cx="8" cy="8" r="8"/><path d="M6 4.5 L11.5 8 L6 11.5Z" fill="#fff"/></svg>Taro Root</li>
    </ul>
  </aside>

  <footer class="site-footer">
    <p class="copyright">Copyright © 2012 Company Name.&nbsp; All Rights Reserved.</p>
    <div class="social-links">
      <span class="social-dot"></span>
      <span class="social-dot"></span>
      <span class="social-dot"></span>
    </div>
  </footer>
  <div class="footer-base"></div>
</body>
</html>
```